10x20 trade show Booth for Software company

This is a tradeshow booth for an event in October. We are a software company that provides integrated communications systems to recruitment companies, called Brightwave. This booth design has 3 different panels. I have attached the guides from the maker of the booth, as well as some brief text to be included and our Logo. In the past, we have always made things way too purple, as our color is purple, but I like the idea of an even mix of purple and white. We are looking for a design that is professional, but creative in the techy style. Simple but capturing what we do.

Target Market(s)

Recruitment companies, sales, decision makers, event attendees.

Industry/Entity Type

Recruitment

Font styles to use
Sans Serif

Colors
6b449b
876aae
b7a5cd
e4daeb
ffffff
5c5c5c
1b1b1b
000000

Requirements
Must have
• Logo included, text included, design template included.
Nice to have
• Maybe some icons or stock photos.
• Geometric design

```html
<!DOCTYPE html>
<html lang="en">
<head>
<meta charset="utf-8">
<title>Brightwave – Trade Show Booth</title>
<link rel="stylesheet" href="https://fonts.googleapis.com/css2?family=Questrial&family=Roboto:wght@400;500;700&display=swap">
<style>
  :root{
    --purple-deep:#6b449b;
    --purple:#876aae;
    --purple-soft:#b7a5cd;
    --lilac:#e4daeb;
    --white:#ffffff;
    --grey:#5c5c5c;
    --ink:#1b1b1b;
    --headline:#4a4440;
    --stage:#f1f0f3;
  }
  *{margin:0;padding:0;box-sizing:border-box}
  html,body{width:1200px;height:638px;overflow:hidden;background:var(--stage)}
  .booth{position:relative;width:1200px;height:638px;font-family:"Roboto",Arial,sans-serif}
  .booth-art{position:absolute;inset:0}
  .benefits{position:absolute;left:66px;top:265px;width:270px;list-style:none}
  .benefit{position:relative;padding-left:22px;margin-bottom:16px}
  .benefit-title{display:block;color:var(--purple-deep);font-weight:500;font-size:12.5px;line-height:15px}
  .benefit-text{display:block;color:var(--grey);font-size:12px;line-height:15px}
  .tick{position:absolute;left:0;top:0;width:15px;height:15px}
  .features{position:absolute;left:950px;top:275px;list-style:none}
  .feature{position:relative;padding-left:25px;margin-bottom:11px;color:var(--headline);font-weight:500;font-size:15px;line-height:19px}
  .feature .tick{top:2px}
  .web{position:absolute;top:541px;color:var(--white);font-size:15.5px;font-weight:500;letter-spacing:2.2px;text-align:center;width:320px}
  .web-left{left:24px}
  .web-right{left:862px;width:313px}
  .brand{position:absolute;left:518px;top:92px;width:172px;height:54px;border-radius:27px;
    background:linear-gradient(180deg,var(--purple) 0%,var(--purple-deep) 100%);
    display:flex;align-items:center;justify-content:center;
    color:var(--white);font-family:"Questrial",Arial,sans-serif;font-size:26px}
  .headline{position:absolute;left:350px;top:164px;width:506px;text-align:center;
    font-family:"Questrial",Arial,sans-serif;font-weight:400;font-size:37px;line-height:40px;color:var(--headline)}
</style>
</head>
<body>
<div class="booth">
  <svg class="booth-art" width="1200" height="638" viewBox="0 0 1200 638">
    <defs>
      <linearGradient id="sideFade" x1="0" y1="58" x2="0" y2="285" gradientUnits="userSpaceOnUse">
        <stop offset="0" stop-color="#7d5ea8"/>
        <stop offset="0.45" stop-color="#8e74b4"/>
        <stop offset="1" stop-color="#ffffff"/>
      </linearGradient>
      <linearGradient id="photoTone" x1="0" y1="0" x2="1" y2="1">
        <stop offset="0" stop-color="#eef0f4"/>
        <stop offset="1" stop-color="#bfc5cf"/>
      </linearGradient>
      <clipPath id="panels">
        <path d="M24 590 V125 Q30 58 200 58 Q330 58 344 95 V590 Z"/>
        <path d="M350 590 V132 Q350 108 374 108 H832 Q856 108 856 132 V590 Z"/>
        <path d="M862 590 V95 Q876 58 1010 58 Q1170 58 1175 125 V590 Z"/>
      </clipPath>
    </defs>

    <g class="panel-surfaces" clip-path="url(#panels)">
      <rect x="0" y="0" width="1200" height="638" fill="var(--white)"/>
      <rect class="side-fade" x="24" y="58" width="320" height="230" fill="url(#sideFade)"/>
      <rect class="side-fade" x="862" y="58" width="313" height="230" fill="url(#sideFade)"/>
      <path class="wave" d="M0 438 C120 470 250 520 350 530 C500 545 720 505 860 440 C960 408 1100 420 1200 446 V600 H0 Z" fill="var(--purple)"/>
      <path class="wave-line" d="M0 450 C120 482 250 532 350 542 C500 557 720 517 860 452 C960 420 1100 432 1200 458" fill="none" stroke="var(--white)" stroke-width="5"/>
    </g>

    <svg x="73" y="83" width="222" height="178" viewBox="0 0 100 80" preserveAspectRatio="none" role="img" aria-label="Photo: recruiters with headsets working at computers">
      <path d="M12 62 C2 60 0 44 8 38 C4 24 16 14 28 18 C34 4 58 2 66 14 C80 8 96 18 92 34 C100 40 100 58 88 62 L22 62 L16 78 L14 62 Z" fill="url(#photoTone)" stroke="var(--white)" stroke-width="2" vector-effect="non-scaling-stroke"/>
    </svg>

    <svg x="436" y="302" width="336" height="270" viewBox="0 0 100 80" preserveAspectRatio="none" role="img" aria-label="Photo: smiling recruiter on the phone at her desk">
      <path d="M12 62 C2 60 0 44 8 38 C4 24 16 14 28 18 C34 4 58 2 66 14 C80 8 96 18 92 34 C100 40 100 58 88 62 L22 62 L16 78 L14 62 Z" fill="url(#photoTone)" stroke="var(--purple-deep)" stroke-width="3" vector-effect="non-scaling-stroke"/>
    </svg>

    <svg x="910" y="83" width="223" height="178" viewBox="0 0 100 80" preserveAspectRatio="none" role="img" aria-label="Photo: recruiter with headset in a bright office">
      <path d="M12 62 C2 60 0 44 8 38 C4 24 16 14 28 18 C34 4 58 2 66 14 C80 8 96 18 92 34 C100 40 100 58 88 62 L22 62 L16 78 L14 62 Z" fill="url(#photoTone)" stroke="var(--white)" stroke-width="2" vector-effect="non-scaling-stroke"/>
    </svg>
  </svg>

  <div class="brand">Brightwave</div>
  <h1 class="headline">Integrated<br>Communications<br>for Recruitment</h1>

  <ul class="benefits">
    <li class="benefit">
      <svg class="tick" viewBox="0 0 16 16"><circle cx="8" cy="8" r="7" fill="none" stroke="var(--purple-deep)" stroke-width="1.4"/><path d="M4.6 8.2 L7.2 10.7 L11.6 5.4" fill="none" stroke="var(--purple-deep)" stroke-width="1.5" stroke-linecap="round" stroke-linejoin="round"/></svg>
      <span class="benefit-title">Increase Productivity</span>
      <span class="benefit-text">Have more quality conversations,<br>leading to more placements<br>in less time.</span>
    </li>
    <li class="benefit">
      <svg class="tick" viewBox="0 0 16 16"><circle cx="8" cy="8" r="7" fill="none" stroke="var(--purple-deep)" stroke-width="1.4"/><path d="M4.6 8.2 L7.2 10.7 L11.6 5.4" fill="none" stroke="var(--purple-deep)" stroke-width="1.5" stroke-linecap="round" stroke-linejoin="round"/></svg>
      <span class="benefit-title">Enhance Data Quality</span>
      <span class="benefit-text">All conversations saved within<br>your CRM, never lose<br>important details.</span>
    </li>
    <li class="benefit">
      <svg class="tick" viewBox="0 0 16 16"><circle cx="8" cy="8" r="7" fill="none" stroke="var(--purple-deep)" stroke-width="1.4"/><path d="M4.6 8.2 L7.2 10.7 L11.6 5.4" fill="none" stroke="var(--purple-deep)" stroke-width="1.5" stroke-linecap="round" stroke-linejoin="round"/></svg>
      <span class="benefit-title">Accelerate training &amp; on-boarding</span>
      <span class="benefit-text">Monitor and coach real-time, reducing<br>time-to-value and attrition.</span>
    </li>
  </ul>

  <ul class="features">
    <li class="feature"><svg class="tick" viewBox="0 0 16 16"><circle cx="8" cy="8" r="7" fill="none" stroke="var(--purple-deep)" stroke-width="1.4"/><path d="M4.6 8.2 L7.2 10.7 L11.6 5.4" fill="none" stroke="var(--purple-deep)" stroke-width="1.5" stroke-linecap="round" stroke-linejoin="round"/></svg>Voice</li>
    <li class="feature"><svg class="tick" viewBox="0 0 16 16"><circle cx="8" cy="8" r="7" fill="none" stroke="var(--purple-deep)" stroke-width="1.4"/><path d="M4.6 8.2 L7.2 10.7 L11.6 5.4" fill="none" stroke="var(--purple-deep)" stroke-width="1.5" stroke-linecap="round" stroke-linejoin="round"/></svg>Texting</li>
    <li class="feature"><svg class="tick" viewBox="0 0 16 16"><circle cx="8" cy="8" r="7" fill="none" stroke="var(--purple-deep)" stroke-width="1.4"/><path d="M4.6 8.2 L7.2 10.7 L11.6 5.4" fill="none" stroke="var(--purple-deep)" stroke-width="1.5" stroke-linecap="round" stroke-linejoin="round"/></svg>Instant Messaging</li>
    <li class="feature"><svg class="tick" viewBox="0 0 16 16"><circle cx="8" cy="8" r="7" fill="none" stroke="var(--purple-deep)" stroke-width="1.4"/><path d="M4.6 8.2 L7.2 10.7 L11.6 5.4" fill="none" stroke="var(--purple-deep)" stroke-width="1.5" stroke-linecap="round" stroke-linejoin="round"/></svg>Unmatched<br>CRM Integration</li>
  </ul>

  <p class="web web-left">www.brightwave-qvtalk.com</p>
  <p class="web web-right">www.brightwave-qvtalk.com</p>
</div>
</body>
</html>
```